Yard Sign Design for luxury design & build company

Looking to have 18" x 24" company yard signs designed.
An update to the business logo might be helpful.
Photos are not necessary but use if you can make inspiring.

Industry: Construction

Looking for a large headline of "Basement Finishing"
Website: www.tamberlyhomes.com
Phone Number (612) 555-0174
FB link: facebook.com/tamberlyhomesmn
Instagram: www.instagram.com/tamberlyhomesmn

Industry/Entity Type

Construction

Colors

Designer to choose colors to be used in the design.

Requirements
Must have
• Impactful high end characteristics
Nice to have
• Depth and detail graphis

```html
<!DOCTYPE html>
<html lang="en">
<head>
<meta charset="utf-8">
<title>Tamberly Homes – Basement Finishing Yard Sign</title>
<link rel="stylesheet" href="https://fonts.googleapis.com/css2?family=Anton&family=Montserrat:wght@600;700;800&display=swap">
<style>
  :root {
    --brand-red: #dc2427;
    --ink: #111111;
    --paper: #ffffff;
    --backdrop: #e9e9e7;
    --photo-warm: #7a6654;
    --photo-light: #b9b3ab;
    --badge: #eeeeee;
  }
  * { margin: 0; padding: 0; box-sizing: border-box; }
  html, body {
    width: 1200px; height: 1002px; overflow: hidden;
    background: var(--backdrop);
    font-family: "Montserrat", sans-serif;
  }
  .yard-sign {
    position: absolute; left: 247px; top: 31px;
    width: 705px; height: 940px;
    background: var(--paper);
    box-shadow: 0 6px 24px rgba(0,0,0,0.18);
    overflow: hidden;
  }
  .sign-header {
    position: absolute; left: 0; top: 0; width: 705px; height: 263px;
    background: var(--brand-red);
  }
  .logo-panel {
    position: absolute; left: 35px; top: 42px; width: 635px; height: 221px;
    background: var(--paper);
    border-radius: 33px 33px 0 0;
    display: flex; align-items: center; justify-content: center; gap: 22px;
  }
  .logo-ring {
    width: 120px; height: 120px; border-radius: 50%;
    border: 6px solid var(--brand-red);
  }
  .logo-name {
    font-weight: 800; font-size: 40px; letter-spacing: 3px;
    color: var(--ink); line-height: 1;
  }
  .headline-band {
    position: absolute; left: 0; top: 263px; width: 705px; height: 338px;
    background: var(--ink);
  }
  .headline-band svg { display: block; }
  .headline-text {
    font-family: "Anton", sans-serif; fill: var(--paper); font-size: 150px;
  }
  .project-photo {
    position: absolute; top: 609px; height: 188px;
  }
  .project-photo.living-room {
    left: 44px; width: 305px;
    background: linear-gradient(160deg, #4b3f36 0%, var(--photo-warm) 55%, #a78a6c 100%);
  }
  .project-photo.game-room {
    left: 355px; width: 308px;
    background: linear-gradient(160deg, #d9d6d1 0%, var(--photo-light) 55%, #7d6a58 100%);
  }
  .contact {
    position: absolute; left: 40px; top: 824px;
    font-weight: 700; color: var(--ink);
  }
  .contact-phone { font-size: 16px; line-height: 22px; }
  .contact-web { font-size: 17px; line-height: 24px; }
  .contact-social {
    display: flex; align-items: center; gap: 6px; margin-top: 6px;
  }
  .social-dot {
    width: 22px; height: 22px; border-radius: 50%; background: var(--ink);
  }
  .social-handle {
    background: var(--brand-red); color: var(--paper);
    font-size: 15px; font-weight: 700; padding: 1px 9px 2px;
    border-radius: 4px; line-height: 19px;
  }
  .review-badge {
    position: absolute; left: 499px; top: 846px; width: 164px; height: 58px;
    background: var(--badge); border-radius: 8px;
  }
</style>
</head>
<body>
  <div class="yard-sign">
    <div class="sign-header">
      <div class="logo-panel">
        <div class="logo-ring"></div>
        <div class="logo-name">TAMBERLY HOMES</div>
      </div>
    </div>

    <div class="headline-band">
      <svg width="705" height="338" viewBox="0 0 705 338">
        <text class="headline-text" x="44" y="164" textLength="619" lengthAdjust="spacingAndGlyphs">BASEMENT</text>
        <text class="headline-text" x="44" y="298" textLength="619" lengthAdjust="spacingAndGlyphs">FINISHING</text>
      </svg>
    </div>

    <div class="project-photo living-room" role="img" aria-label="Finished basement living room with sectional sofas, fireplace and wet bar"></div>
    <div class="project-photo game-room" role="img" aria-label="Finished basement game room with pool table, stone fireplace and kitchenette"></div>

    <div class="contact">
      <div class="contact-phone">Call (612) 555-0174</div>
      <div class="contact-web">www.tamberlyhomes.com</div>
      <div class="contact-social">
        <span class="social-dot"></span>
        <span class="social-handle">tamberlyhomesmn</span>
      </div>
    </div>

    <div class="review-badge"></div>
  </div>
</body>
</html>
```